Rate Card

We wish to update our rate card flyer.I have uploaded a copy of our current version, which has a black background but we want to redesign this with a cleaner and fresh look with a white background. Our new logo also needs to be used.

The stats on the why choose us need to be updated also.

- 8,000+ sales agreed
- £2.1bn sales value
- £41m savings
- 97.5% recommended
- 5,000 client testimonials

We would like a new look to this double sided flyer.

This is an urgent requirement so anyone that posts a design we like quickly will more than likely get this order!

```html
<!DOCTYPE html>
<html lang="en">
<head>
<meta charset="utf-8">
<title>Keyway Homes Rate Card</title>
<link href="https://fonts.googleapis.com/css2?family=Fira+Sans+Condensed:ital,wght@0,700;1,600;1,700&family=Lato:ital,wght@0,400;0,700;0,900;1,400;1,700;1,900&display=swap" rel="stylesheet">
<style>
:root{
  --pink:#e6388f;
  --pink-dark:#b5136a;
  --pink-light:#f46fb2;
  --cream:#f8f4ec;
  --ink:#2b2b2b;
  --blue:#2a8fd6;
  --row-blue:#a9e1f6;
  --row-orange:#fbb878;
  --row-green:#c9e68c;
  --grey:#5a5a5a;
  --portal:#3c2a5c;
  --badge-a:#7a3f9a;
  --badge-b:#2aa6df;
  --badge-c:#b3162b;
  --badge-d:#c8102e;
}
*{box-sizing:border-box;margin:0;padding:0}
html,body{width:843px;height:1200px;overflow:hidden;background:#fff}
body{position:relative;font-family:"Lato",sans-serif;color:var(--ink)}
.panel{position:absolute;left:35px;width:774px;background:var(--cream);border:2px solid var(--pink)}
.panel--fees{top:14px;height:581px}
.panel--why{top:603px;height:584px}
.band{position:absolute;left:0;right:0;display:flex;align-items:center;justify-content:center;color:#fff;
  background:linear-gradient(180deg,var(--pink-light) 0%,var(--pink) 45%,var(--pink-dark) 100%)}
.band--head{top:0;height:58px;font-family:"Fira Sans Condensed",sans-serif;font-weight:700;font-size:32px}
.band--foot{bottom:0;height:56px;font-style:italic;font-size:19px}
.band--url{letter-spacing:2.5px;font-size:19px}
.fee-table{position:absolute;left:20px;top:110px;border-collapse:collapse;font-size:19px}
.fee-table td,.fee-table th{border:2px solid #333;padding:0 16px;text-align:left;height:52px}
.fee-table th{font-family:"Fira Sans Condensed",sans-serif;font-weight:600;font-style:italic;color:#fff;font-size:21px;padding:0 10px;
  background:linear-gradient(180deg,var(--pink-light),var(--pink))}
.fee-table tr.head th{height:54px;padding:0 16px}
.fee-table th.blank{background:#fff}
.row-blue td{background:var(--row-blue)}
.row-orange td{background:var(--row-orange)}
.row-green td{background:var(--row-green);font-size:18px}
.footnote{position:absolute;right:26px;top:349px;font-size:13px}
.advertised{position:absolute;left:24px;top:402px;color:var(--blue);font-weight:900;font-style:italic;font-size:18px}
.portals{position:absolute;left:24px;top:446px;display:flex;gap:30px;align-items:center;font-weight:900;font-size:22px;color:var(--portal)}
.brand{position:absolute;left:540px;top:428px;display:flex;align-items:center;gap:10px}
.brand__mark{width:30px;height:30px;background:var(--pink)}
.brand__name{font-weight:900;font-size:25px;color:var(--grey);line-height:1}
.brand__tag{font-size:13px;color:var(--grey);margin-top:5px}
.stats-title,.service-title{position:absolute;color:var(--pink);font-weight:700;font-size:21px;line-height:28px}
.stats-title{left:37px;top:86px}
.service-title{left:390px;top:113px}
.ticks{position:absolute;list-style:none;font-size:16.5px;line-height:23.4px}
.ticks li{position:relative;padding-left:14px}
.ticks li::before{content:"";position:absolute;left:0;top:8px;border-left:6px solid var(--pink);border-top:4px solid transparent;border-bottom:4px solid transparent}
.ticks--stats{left:37px;top:151px;width:340px}
.ticks--service{left:390px;top:151px;width:370px}
.featured-title{position:absolute;left:37px;top:405px;color:var(--blue);font-weight:900;font-style:italic;font-size:18px}
.badges{position:absolute;left:37px;top:442px;display:flex;gap:7px;align-items:center}
.contact{position:absolute;left:485px;top:383px;display:flex;gap:20px}
.contact__mark{width:72px;height:72px;background:var(--pink);margin-top:10px}
.contact__text{font-style:normal;font-size:12.5px;line-height:12.6px;color:var(--ink)}
.contact__text .accent{color:var(--pink)}
</style>
</head>
<body>
<section class="panel panel--fees">
  <div class="band band--head">Fee Menu</div>
  <table class="fee-table">
    <tr class="head"><th class="blank" style="width:171px"></th><th style="width:142px">Upfront</th><th style="width:205px">Completion</th><th style="width:211px">Total</th></tr>
    <tr class="row-blue"><th>No Commission</th><td>£495+VAT</td><td>£0</td><td>£495+VAT</td></tr>
    <tr class="row-orange"><th>Commission</th><td>£195+VAT</td><td>£795+VAT</td><td>£990+VAT</td></tr>
    <tr class="row-green"><th>No Sale-No Fee</th><td>£0</td><td>we’ll beat any quote*</td><td>we’ll beat any quote*</td></tr>
  </table>
  <p class="footnote">* subject to a minimum fee of £1000</p>
  <p class="advertised">Your property advertised on :</p>
  <div class="portals"><span>Propertyline</span><span>Homeseek</span><span>PrimeSpot</span></div>
  <div class="brand">
    <div class="brand__mark"></div>
    <div><div class="brand__name">Keyway Homes</div><div class="brand__tag">the smarter way to sell</div></div>
  </div>
  <div class="band band--foot">Keyway Homes : The Smarter Way to Sell</div>
</section>

<section class="panel panel--why">
  <div class="band band--head">Why Choose Us?</div>
  <h2 class="stats-title">Strength in numbers<br>since our launch in 2003</h2>
  <ul class="ticks ticks--stats">
    <li>8,000+ sales agreed</li>
    <li>£2.1bn sales value</li>
    <li>£41m savings</li>
    <li>£4,500 average fee SAVING vs high street</li>
    <li>97.5% recommended</li>
    <li>5,000 client testimonials</li>
    <li>9/10 average client rating</li>
    <li>Rated no. 2 estate agent in the UK<br>by the independent Verdict Hub</li>
  </ul>
  <h2 class="service-title">Customer Service</h2>
  <ul class="ticks ticks--service">
    <li>Personal account manager with direct dial</li>
    <li>Online account to track your progress</li>
    <li>All staff are NPEA qualified</li>
    <li>Weekly activity reports keep you in the loop</li>
    <li>Live web chat facility after hours</li>
    <li>Full personal estate agency service from<br>instruction to completion</li>
  </ul>
  <p class="featured-title">As Featured on :</p>
  <div class="badges">
    <svg width="146" height="40" role="img" aria-label="Partner badge"><rect width="146" height="40" rx="6" fill="var(--badge-a)"/></svg>
    <svg width="38" height="40" role="img" aria-label="Partner badge"><rect width="38" height="40" fill="var(--badge-b)"/></svg>
    <svg width="48" height="40" role="img" aria-label="Partner badge"><rect width="48" height="40" fill="var(--badge-c)"/></svg>
    <svg width="92" height="40" role="img" aria-label="Partner badge"><rect width="92" height="40" fill="var(--badge-d)"/></svg>
  </div>
  <div class="contact">
    <div class="contact__mark"></div>
    <address class="contact__text">
      <span class="accent">Keyway Homes</span><br>
      Estate Offices<br>
      Millbrook Farm<br>
      Millbrook Lane<br>
      Millbrook<br>
      Essex&nbsp; CM9 2XY<br>
      T 0800 123 4567<br>
      <span class="accent">www.keywayhomes.co.uk</span>
    </address>
  </div>
  <div class="band band--foot band--url">www.keywayhomes.co.uk</div>
</section>
</body>
</html>
```